Harbinger and Lantern Website

We are a private investigation that people turn to when they seek answers. We provide all types of investigation services as well as security and debt collection but mainly we specialise in digital forensic investigation. This site will be the first representation that potential clients see. We need a site that can work on all browsers so not too many animations. The theme we are going for is "Pallor" the TV show but keeping the law enforcement look. We want it to expand on the logo of our company that is strength and pride (refer to files attached). The logo and mission statement must stand out.
The relevant info is attached in .doc documents
Updates

Hi,

I have uploaded a slightly different version of the logo and I do prefer the new version and made a FEW but important updates and additions to the website info. Sorry for the inconvenience.

Hi, 

Sorry just one last thing can you please put the following on the website 'Harbinger and Lantern is a South Australian owned business and we service all of Australia.' 

I have increased the budget.

Hi,

I've increased the budget slightly. I will continue to increase it as long as the quality of designs match it.

I have increased the budget. I will increase it more if I see some designs that warrant the increase.

I have extended the deadline by 3 days.

Hi,

Forget the brief and please take a look at this link and that is the type of design I want. I want people to look at it and think modern, professional, digital, forensic investigation. I have not seen anything that makes me think "wow" so please submit some new designs. I will increase the budget when I start to see designs that I like. 

regarding the last message, this is the link

https://www.vantorel-example.org

Reason: Have not seen anything that stands out from the rest.

Reason: To let designers finish off their current concepts that they may be working on.

Target Market(s)

Average to corporate people seeking professionalism and a firm that can supply answers that traditional law enforcement agencies fail to provide

Industry/Entity Type

Security

Requirements
Must have
• A professional QRD, Southern Tablelands Constabulary website look mixed with a theme from the TV show "Pallor" and the ability to download the business cards (refer to attached files)
Should not have
• cartoon images and anything relating to Ambrose Pettigrew

```html
<!DOCTYPE html>
<html lang="en">
<head>
<meta charset="utf-8">
<title>Harbinger and Lantern — Private Intelligence</title>
<link rel="stylesheet" href="https://fonts.googleapis.com/css2?family=Signika:wght@300;400;600&family=Open+Sans:wght@400;600;700&family=Russo+One&display=swap">
<style>
:root{
  --ink:#1b1b1b;
  --page:#222;
  --panel:#2a2a2a;
  --gold:#e9c233;
  --gold-deep:#a47a10;
  --gold-text:#a4780a;
  --white:#fff;
  --muted:#d9d9d9;
  --line:#4a4a4a;
  --nav:#1e1e1e;
}
*{margin:0;padding:0;box-sizing:border-box}
html,body{width:682px;height:1200px;overflow:hidden;background:var(--page)}
body{font-family:"Open Sans",Arial,sans-serif;color:var(--white)}
.site{position:relative;width:682px;height:1200px;overflow:hidden;
  background:linear-gradient(180deg,#2b2b2b 0,#262626 400px,#1e1e1e 975px)}
.header-glow{position:absolute;left:0;top:0;width:682px;height:420px;
  background:radial-gradient(ellipse 420px 240px at 340px 110px,#fff4a8 0,#f0cc3a 35%,#b8880f 70%,rgba(40,32,10,0) 100%),
  linear-gradient(180deg,#c89a1a 0,#8a6510 260px,rgba(38,38,38,0) 420px)}
.top-strip{position:absolute;left:0;top:0;width:682px;height:8px;background:#1a1a1a}
.brand{position:absolute;left:34px;top:24px;display:flex;align-items:center;gap:8px}
.brand-mark{width:22px;height:22px;border-radius:50%;background:#3a2a05}
.brand-name{font-family:"Signika",sans-serif;font-weight:600;font-size:16px;color:#3a2a05;width:130px;line-height:1.15}
.contact-line{position:absolute;left:384px;font-family:"Signika",sans-serif;color:#222;font-size:12.5px}
.contact-line b{position:absolute;left:86px;font-weight:600;white-space:nowrap}
.call{top:23px;font-size:13px}.call b{font-size:15px;top:-2px}
.mail{top:42px}.mail b{font-size:9.5px;top:3px}
.hours-box{position:absolute;left:378px;top:63px;width:277px;height:53px;background:var(--white);border-radius:6px;
  padding:5px 0 0 9px;font-size:8.3px;line-height:16px;color:#222;font-weight:600}
.hours-box em{font-style:normal;color:var(--gold-text)}
.main-nav{position:absolute;left:20px;top:125px;width:641px;height:33px;background:var(--nav);border-radius:4px 4px 0 0;display:flex}
.main-nav a{font-family:"Signika",sans-serif;font-size:12px;color:var(--white);text-decoration:none;padding:9px 14px 0 24px;border-right:1px solid #333;height:33px}
.slider-frame{position:absolute;left:20px;top:157px;width:641px;height:207px;background:var(--white)}
.slide{position:absolute;left:9px;top:7px;width:624px;height:190px;
  background:radial-gradient(ellipse at 45% 30%,#6a7896 0,#3a4662 45%,#1c2438 100%)}
.slide-title{position:absolute;left:0;width:100%;top:58px;text-align:center;font-family:"Russo One",sans-serif;font-size:47px;letter-spacing:2px;color:#d6dae0}
.slide-caption{position:absolute;left:0;bottom:0;width:100%;height:43px;background:rgba(20,24,34,.75)}
.slide-caption h2{position:absolute;left:50px;top:8px;font-family:"Signika",sans-serif;font-weight:300;font-size:24px;color:var(--gold)}
.slide-caption p{position:absolute;left:318px;top:9px;font-size:10px;line-height:12px;width:280px}
.arrow{position:absolute;top:85px;width:18px;height:22px;background:#ddd;border-radius:3px}
.arrow.prev{left:0}.arrow.next{right:0}
.arrow svg{display:block;margin:6px auto 0}
.service{position:absolute;width:200px}
.service-photo{width:200px;height:90px;border:1px solid #ddd;position:relative}
.service-photo h3{position:absolute;left:0;bottom:0;width:100%;height:23px;background:linear-gradient(#444,#222);
  font-family:"Signika",sans-serif;font-weight:400;font-size:14px;padding:3px 0 0 13px}
.service p{font-size:7.7px;line-height:11.4px;color:var(--muted);padding:6px 8px 0 9px}
.info-col{position:absolute;top:718px;height:256px}
.info-col h2{font-family:"Signika",sans-serif;font-weight:400;font-size:15px;margin-bottom:16px}
.about p{font-size:7.7px;line-height:11.6px;color:var(--muted);text-align:justify;margin-bottom:5px}
.col-divider{position:absolute;top:718px;width:6px;height:258px;background:linear-gradient(90deg,rgba(0,0,0,.4),rgba(255,255,255,.05))}
.quals h3{font-size:8.5px;font-weight:600;margin-bottom:4px}
.quals li{list-style:none;font-size:7.7px;line-height:14px;color:var(--muted)}
.btn{display:inline-block;margin-top:16px;background:linear-gradient(#444,#111);border-radius:8px;font-size:7.5px;font-weight:700;padding:4px 7px}
.news-item{display:flex;gap:6px;margin-bottom:21px}
.news-thumb{width:55px;height:47px;border:2px solid #ccc;flex:none}
.news-item h4{font-family:"Signika",sans-serif;font-weight:400;font-size:9.5px;margin-bottom:2px}
.news-item p{font-size:7.5px;line-height:10.8px;color:var(--muted)}
.news-item small{display:block;font-size:7.5px;font-weight:700;margin-top:4px}
.footer{position:absolute;left:0;top:976px;width:682px;height:224px;background:linear-gradient(#2e2e2e,#1a1a1a)}
.footer h2{position:absolute;left:44px;top:16px;font-family:"Signika",sans-serif;font-weight:400;font-size:13px}
.link-col{position:absolute;top:41px}
.link-col a{display:block;font-size:8px;color:var(--white);text-decoration:none;height:19.4px;line-height:19px;border-bottom:1px solid #3a3a3a}
.footer-rule{position:absolute;left:44px;top:176px;width:594px;height:1px;background:#333}
.copyright{position:absolute;left:44px;top:189px;font-size:8px}
</style>
</head>
<body>
<div class="site">
  <div class="header-glow"></div>
  <div class="top-strip"></div>

  <div class="brand"><span class="brand-mark"></span><span class="brand-name">Harbinger and Lantern</span></div>

  <div class="contact-line call">Call us Quickly <b>0400 123 456</b></div>
  <div class="contact-line mail">Email Us: <b>managers@harbingerlantern.example</b></div>
  <div class="hours-box">
    Contact hours : <em>24 hours</em> a day<br>
    You can also find us in the <em>Local Directory</em>.<br>
    Please feel free to <em>E-mail us</em> for a <em>free info-flyer</em> with no obligation.
  </div>

  <nav class="main-nav">
    <a href="#">Home</a><a href="#">About Us</a><a href="#">Services</a><a href="#">Security</a><a href="#">Download</a><a href="#">Contact</a>
  </nav>

  <div class="slider-frame">
    <div class="slide" role="img" aria-label="Dark blue digital backdrop with a handprint and binary numbers">
      <div class="slide-title">INVESTIGATION</div>
      <div class="slide-caption">
        <h2>PRIVATE INTELLIGENCE</h2>
        <p>We act in accordance with the Industry certified processes to deliver the best</p>
      </div>
      <span class="arrow prev"><svg width="6" height="10"><path d="M5 0 0 5 5 10z" fill="#333"/></svg></span>
      <span class="arrow next"><svg width="6" height="10"><path d="M1 0 6 5 1 10z" fill="#333"/></svg></span>
    </div>
  </div>

  <section class="service" style="left:27px;top:385px">
    <div class="service-photo" role="img" aria-label="Officer questioning a man across a desk" style="background:linear-gradient(90deg,#c9c2b8,#c0552a 60%,#d8d2ca)"><h3>Unsolved Cases</h3></div>
    <p>if you are unsatisfied with the investigation performed by other private investigation agencies and or law enforcement we will continue the investigation until we can provide you with the quality investigation and answers that you seek.</p>
  </section>
  <section class="service" style="left:240px;top:385px">
    <div class="service-photo" role="img" aria-label="Distressed man sitting on stadium steps" style="background:linear-gradient(#6b6b6b,#2c2c2c)"><h3>Bullying/Stalking</h3></div>
    <p>Is someone stalking you or bullying you? Well we will get the proof and evidence whether it be online and or in real life so that you can take it to the authorities and get them to put a stop to the stalking.</p>
  </section>
  <section class="service" style="left:452px;top:385px">
    <div class="service-photo" role="img" aria-label="Worried young couple" style="background:linear-gradient(90deg,#5a463c,#9a7a68 50%,#4a3c34)"><h3>Missing Persons</h3></div>
    <p>We will help locate family members, friends and anyone who you care about that have gone missing. Anything from run away to abduction we will use all our resources to help locate these people.</p>
  </section>

  <section class="service" style="left:27px;top:557px">
    <div class="service-photo" role="img" aria-label="Police officers with children outdoors" style="background:linear-gradient(90deg,#3a4a6a,#8a7a6a 50%,#5a5a4a)"><h3>Child recovery</h3></div>
    <p>Our wide range of resources, skills and experience will help you find your children and get them back to you safe and sound.</p>
  </section>
  <section class="service" style="left:240px;top:557px">
    <div class="service-photo" role="img" aria-label="Judge's gavel close up" style="background:radial-gradient(circle at 30% 40%,#c08a50,#5a3418 70%)"><h3>Con Men and Con Women</h3></div>
    <p style="padding-left:17px">If you suspect a family member and or friend is being conned by someone, we can gather the proof through many avenues including background checks and surveillance both in real life and online.</p>
  </section>
  <section class="service" style="left:452px;top:557px">
    <div class="service-photo" role="img" aria-label="Couple standing back to back" style="background:linear-gradient(90deg,#fff,#ddd 40%,#555 60%,#fff)"><h3>Pre-marital checks</h3></div>
    <p style="padding-left:17px">We will help put your mind at rest that the person you are about to marry is who they say they are and are loyal.</p>
  </section>

  <section class="info-col about" style="left:30px;width:195px">
    <h2>WHo We are?</h2>
    <p>What makes Harbinger and Lantern stand out from the rest is we believe investigation is not just a service, it is a science and we are the scientists of investigation. We use psychology and sociology to carry out our investigations. We observe human behavior and how society interacts and then apply the principles of investigation. By doing so we have an extremely high success rate in all areas of investigation. We also provide specialized forensic services that law enforcement and military provide.</p>
    <p>Harbinger is a private investigation and intelligence group and alternative to law enforcement agencies. We conduct all types of investigations including factual, forensic and surveillance.</p>
  </section>
  <div class="col-divider" style="left:233px"></div>

  <section class="info-col quals" style="left:251px;width:190px">
    <h2>Our Qualification</h2>
    <h3>Qualification listed :</h3>
    <ul>
      <li>Bachelor of behavioral Studies (Psychology)</li>
      <li>Masters of International Securities</li>
      <li>Graduate certificate of Science</li>
      <li>Bachelor of Accounting</li>
      <li>Master of Information Management</li>
      <li>Master of Criminology and Criminal Justice</li>
    </ul>
    <span class="btn">READ MORE</span>
  </section>
  <div class="col-divider" style="left:444px"></div>

  <section class="info-col news" style="left:456px;width:200px">
    <h2 style="margin-bottom:12px">Featued News</h2>
    <article class="news-item"><div class="news-thumb" role="img" aria-label="Mounted police officer" style="background:#7a8a6a"></div>
      <div><h4>Headline goes here</h4><p>Brightwave Studio provide you with an attractive and most convincing website to enhance</p><small>Read More &nbsp;|&nbsp; Posted on &nbsp;20/03/2012</small></div></article>
    <article class="news-item"><div class="news-thumb" role="img" aria-label="Person in a hat in shadow" style="background:#5a4a3a"></div>
      <div><h4>Headline goes here</h4><p>Brightwave Studio provide you with an attractive and most convincing website to enhance</p><small>Read More &nbsp;|&nbsp; Posted on &nbsp;20/03/2012</small></div></article>
    <article class="news-item"><div class="news-thumb" role="img" aria-label="Woman looking down" style="background:#a8a8b0"></div>
      <div><h4>Headline goes here</h4><p>Brightwave Studio provide you with an attractive and most convincing website to enhance</p><small>Read More &nbsp;|&nbsp; Posted on &nbsp;20/03/2012</small></div></article>
  </section>

  <footer class="footer">
    <h2>Quick links</h2>
    <div class="link-col" style="left:44px;width:100px"><a>Main Page</a><a>About Out Company</a><a>Services Oveview</a><a>FAQ</a><a>Support</a><a style="border:0">Security</a></div>
    <div class="link-col" style="left:173px;width:60px"><a>Testimonials</a><a>News</a><a>Support</a><a>Security</a></div>
    <div class="link-col" style="left:278px;width:140px"><a>Success Storeis</a><a>Apply</a><a>Fill our Form</a><a>Private Investigation &amp; Intelligence</a></div>
    <div class="link-col" style="left:424px;width:100px"><a>Want A home Detective</a><a>Branches</a><a>History</a><a>Auditing</a></div>
    <div class="link-col" style="left:537px;width:100px"><a>Want A home Detective</a><a>Branches</a><a>History</a><a>Auditing</a></div>
    <div class="footer-rule"></div>
    <p class="copyright">© 2012 Company Name &nbsp;|&nbsp; All right reserved</p>
  </footer>
</div>
</body>
</html>
```